Poster design for equestrian event
photoshop horse and rider in to the poster with a building ..
see poster that i add to make the same..
The colors of the event are DARK green and grey

also please add the logo's

```html
<!DOCTYPE html>
<html lang="en">
<head>
<meta charset="utf-8">
<title>Horse Show Poster</title>
<link href="https://fonts.googleapis.com/css2?family=Cinzel:wght@400;600;700&display=swap" rel="stylesheet">
<style>
  :root {
    --paper: #efeee9;
    --green-dark: #0e4637;
    --green-deep: #0a3a2d;
    --grey: #9c9c9b;
    --grey-light: #b4b4b2;
    --cream: #ecebe4;
    --photo-warm: #a9774f;
    --photo-navy: #26304a;
    --photo-stone: #c9c3b8;
  }
  * { box-sizing: border-box; margin: 0; padding: 0; }
  html, body { width: 992px; height: 1200px; overflow: hidden; background: var(--paper); }
  .poster {
    position: relative;
    width: 992px;
    height: 1200px;
    background: var(--paper);
    font-family: "Cinzel", serif;
    overflow: hidden;
  }
  .bands { position: absolute; inset: 0; width: 992px; height: 1200px; }
  .title-horse {
    position: absolute;
    left: 22px;
    top: 180px;
    font-size: 232px;
    font-weight: 600;
    line-height: 1;
    letter-spacing: 2px;
    color: var(--green-dark);
    transform: rotate(-7deg);
    transform-origin: left bottom;
  }
  .title-show {
    position: absolute;
    left: 713px;
    top: 272px;
    font-size: 56px;
    font-weight: 600;
    color: var(--grey);
    transform: rotate(-7deg);
  }
  .hero-photo {
    position: absolute;
    left: 110px;
    top: 290px;
    width: 680px;
    height: 600px;
  }
  .brand {
    position: absolute;
    display: flex;
    flex-direction: column;
    align-items: center;
    gap: 10px;
    color: var(--green-dark);
    font-weight: 600;
  }
  .brand-mark {
    border-radius: 50%;
    background: var(--grey);
  }
  .brand--host { left: 760px; top: 352px; width: 200px; font-size: 24px; }
  .brand--host .brand-mark { width: 62px; height: 62px; }
  .brand--event { left: 70px; top: 860px; width: 220px; font-size: 20px; }
  .brand--event .brand-mark { width: 60px; height: 60px; background: var(--green-dark); }
  .sold-tag {
    position: absolute;
    left: -20px;
    top: 1000px;
    width: 440px;
    height: 150px;
    transform: rotate(-14deg);
  }
  .sold-tag svg { position: absolute; inset: 0; }
  .sold-tag-text {
    position: absolute;
    left: 60px;
    top: 18px;
    width: 330px;
    text-align: center;
    color: var(--cream);
    line-height: 1;
  }
  .sold-tag-text .tag-line { font-size: 17px; letter-spacing: 1px; }
  .sold-tag-text .tag-main { font-size: 52px; font-weight: 600; margin: 6px 0 4px; }
  .booking {
    position: absolute;
    left: 470px;
    top: 1030px;
    width: 490px;
    text-align: center;
    color: var(--cream);
  }
  .booking-title { font-size: 66px; font-weight: 600; letter-spacing: 1px; line-height: 1; }
  .booking-sub { font-size: 22px; font-weight: 600; letter-spacing: 1px; margin-top: 18px; }
</style>
</head>
<body>
<main class="poster">
  <svg class="bands" viewBox="0 0 992 1200" aria-hidden="true">
    <defs>
      <linearGradient id="topBandShade" x1="0" y1="0" x2="1" y2="0">
        <stop offset="0" stop-color="#8f8f8e"/>
        <stop offset="1" stop-color="#a3a3a2"/>
      </linearGradient>
    </defs>
    <polygon points="0,0 992,0 992,34 0,231" fill="url(#topBandShade)"/>
    <polygon points="0,1133 992,944 992,1200 0,1200" fill="var(--green-dark)"/>
  </svg>

  <h1 class="title-horse">HORSE</h1>
  <div class="title-show">SHOW</div>

  <svg class="hero-photo" viewBox="0 0 680 600" role="img" aria-label="Photograph of a show jumping rider in a navy jacket on a bay horse decorated with rosettes, in front of a wooden-roofed stone building">
    <defs>
      <linearGradient id="photoFade" x1="0" y1="0" x2="0" y2="1">
        <stop offset="0" stop-color="white" stop-opacity="1"/>
        <stop offset="0.78" stop-color="white" stop-opacity="1"/>
        <stop offset="1" stop-color="white" stop-opacity="0"/>
      </linearGradient>
      <mask id="photoMask">
        <rect width="680" height="600" fill="url(#photoFade)"/>
      </mask>
      <linearGradient id="buildingTone" x1="0" y1="0" x2="0" y2="1">
        <stop offset="0" stop-color="#b08865"/>
        <stop offset="0.3" stop-color="var(--photo-stone)"/>
        <stop offset="1" stop-color="#ddd8cf"/>
      </linearGradient>
      <linearGradient id="riderTone" x1="0" y1="0" x2="0" y2="1">
        <stop offset="0" stop-color="var(--photo-navy)"/>
        <stop offset="0.35" stop-color="var(--photo-warm)"/>
        <stop offset="1" stop-color="#7d5a44"/>
      </linearGradient>
    </defs>
    <g mask="url(#photoMask)">
      <rect x="0" y="250" width="680" height="330" fill="url(#buildingTone)"/>
      <rect x="200" y="20" width="280" height="560" rx="40" fill="url(#riderTone)"/>
    </g>
  </svg>

  <div class="brand brand--host">
    <span class="brand-mark"></span>
    <span class="brand-name">H.V. Elderhout</span>
  </div>

  <div class="brand brand--event">
    <span class="brand-mark"></span>
    <span class="brand-name">Oosterveld Show</span>
  </div>

  <div class="sold-tag">
    <svg viewBox="0 0 440 150" aria-hidden="true">
      <polygon points="0,0 380,0 440,75 380,150 0,150" fill="var(--grey)"/>
    </svg>
    <div class="sold-tag-text">
      <div class="tag-line">CASTLE &amp; RESERVED SEATING</div>
      <div class="tag-main">SOLD OUT</div>
      <div class="tag-line">FOR SATURDAY 24 JULY</div>
    </div>
  </div>

  <div class="booking">
    <div class="booking-title">BOOK NOW</div>
    <div class="booking-sub">GENERAL ENTRY &amp; VIP HOSPITALITY</div>
  </div>
</main>
</body>
</html>
```